Rw construct holdings pty ltd

This is a development and construction company. Website can be set up on our domain rwbuildgroup.net if we could change the domain to rwbuildgroup.com.au would be great

Want the page to have eye catching designs, red, black and white are the preffered colours.

Check out www.tolumine.com.au it is my former company with my partner which i am now venturing out on my own, that is the perfect example of the website i want even allot of the information would be the same

Industry/Entity Type

Construction

Coding

Coded - Design and coding required

Number of Pages Required

5+ page

Requirements
Must have
• Company logo eye catching designs

```html
<!DOCTYPE html>
<html lang="en">
<head>
<meta charset="utf-8">
<title>RW Build Group</title>
<link href="https://fonts.googleapis.com/css2?family=Lato:wght@400;700;900&display=swap" rel="stylesheet">
<style>
:root{
  --red:#e0321f;
  --black:#0c0c0c;
  --ink:#1a1a1a;
  --grey:#6b6b6b;
  --light:#f1f1f1;
  --white:#ffffff;
}
*{margin:0;padding:0;box-sizing:border-box}
html,body{width:1200px;height:2992px;overflow:hidden}
body{position:relative;background:var(--white);font-family:"Lato",Arial,sans-serif;color:var(--ink)}
.abs{position:absolute}
.eyebrow{font-size:9px;font-weight:700;color:var(--red);letter-spacing:1px;text-transform:uppercase}
.btn{display:inline-block;background:var(--red);color:var(--white);font-size:9px;font-weight:700;letter-spacing:1px;text-transform:uppercase;padding:9px 20px;white-space:nowrap}
.body-copy{font-size:9px;line-height:1.6;color:var(--grey)}
.photo{display:block}

/* header */
.site-header{top:0;left:0;width:1200px;height:60px;z-index:3}
.brand{display:flex;align-items:center;gap:8px;color:var(--white);font-size:10px;font-weight:700;letter-spacing:1px;white-space:nowrap}
.brand-dot{width:22px;height:22px;border-radius:50%;background:var(--red);flex:none}
.site-header .brand{position:absolute;left:368px;top:18px}
.main-nav{position:absolute;left:540px;top:24px;display:flex;gap:28px;font-size:9px;color:var(--white);text-transform:uppercase;letter-spacing:1px}
.site-header .btn{position:absolute;left:796px;top:18px;padding:7px 16px}

/* hero */
.hero{top:0;left:0;width:1200px;height:400px;background:linear-gradient(180deg,#2b2622 0%,#4b4039 55%,#6a5a4c 100%)}
.hero-title{left:372px;top:140px;font-size:34px;line-height:1.15;font-weight:400;color:var(--white)}
.hero .btn{left:372px;top:232px}

/* intro */
.intro{top:400px;left:0;width:1200px;height:500px}
.intro-photo{left:388px;top:48px;width:240px;height:192px;background:linear-gradient(135deg,#d9d4cc,#8e8478 60%,#3d3834)}
.intro-card{left:600px;top:88px;width:260px;height:224px;background:var(--white);padding:24px 26px}
.intro-card h2{font-size:20px;line-height:1.2;font-weight:400;margin:8px 0 10px}
.intro-card .btn{margin-top:14px}

/* values */
.values{top:840px;left:0;width:1200px;height:480px;background:var(--light)}
.values-text{left:372px;top:30px;width:290px}
.values-text h2{font-size:20px;line-height:1.25;font-weight:400;margin-top:8px}
.value-grid{left:372px;top:160px;width:270px;display:grid;grid-template-columns:1fr 1fr;gap:22px 24px}
.value-grid h3{font-size:9px;font-weight:700;color:var(--red);margin-bottom:4px}
.value-grid h3::before{content:"";display:block;width:14px;height:2px;background:var(--red);margin-bottom:6px}
.stair-photo{left:660px;top:100px;width:200px;height:360px;background:linear-gradient(160deg,#efece7,#c9b9a3 55%,#9c7e5c)}

/* quality */
.house-photo{left:368px;top:1252px;width:232px;height:220px;background:linear-gradient(180deg,#6c6f78,#8a6a52 60%,#3a2c22)}
.quality-card{left:600px;top:1312px;width:260px;height:288px;background:var(--black);color:var(--white);padding:30px 26px}
.quality-card h2{font-size:19px;line-height:1.25;font-weight:400;margin:8px 0 14px}
.quality-card .body-copy{color:#a9a9a9}
.quality-card .btn{margin-top:18px}

/* portfolio */
.portfolio-band{top:1700px;left:0;width:1200px;height:520px;background:var(--light)}
.portfolio-title{left:600px;top:1650px;width:270px;font-size:17px;line-height:1.3;font-weight:400}
.tile{background:linear-gradient(135deg,#3b3634,#1f1c1b)}
.tile span{position:absolute;left:14px;bottom:12px;font-size:9px;color:var(--white);letter-spacing:.5px}
.tile-a{left:368px;top:1728px;width:192px;height:220px}
.tile-b{left:580px;top:1780px;width:280px;height:168px;background:linear-gradient(135deg,#5a5452,#2c2725)}
.tile-c{left:368px;top:1968px;width:280px;height:224px;background:linear-gradient(135deg,#4a4e55,#23252a)}
.tile-d{left:660px;top:1960px;width:200px;height:232px;background:linear-gradient(135deg,#3f3630,#1b1714)}

/* testimonials */
.testimonials{top:2252px;left:0;width:1200px;height:268px;background:var(--black)}
.testimonials-head{left:368px;top:34px;width:300px;color:var(--white)}
.testimonials-head h2{font-size:17px;line-height:1.3;font-weight:400;margin-top:6px}
.arrows{left:780px;top:36px;display:flex;gap:8px}
.arrows div{width:36px;height:24px;background:var(--red);display:flex;align-items:center;justify-content:center}
.review-row{left:368px;top:2380px;display:flex;gap:18px}
.review{width:186px;height:160px;background:var(--white);padding:22px 16px;box-shadow:0 6px 16px rgba(0,0,0,.12);position:relative}
.review .body-copy{padding-right:30px}
.review .quote{position:absolute;right:14px;top:10px;font-size:40px;font-weight:900;color:var(--red);line-height:1}
.review .author{margin-top:14px;font-size:9px;font-weight:700;color:var(--ink)}

/* contact */
.contact{top:2580px;left:0;width:1200px;text-align:center}
.contact h2{font-size:19px;line-height:1.35;font-weight:400}
.contact-form{left:420px;top:2660px;width:360px;display:grid;grid-template-columns:1fr 1fr;gap:26px 24px}
.field{border-bottom:1px solid #cfcfcf;font-size:9px;color:#9a9a9a;padding-bottom:6px}
.field.wide{grid-column:1 / 3;height:40px}
.contact-submit{left:564px;top:2802px;padding:8px 26px}

/* footer */
.site-footer{top:2864px;left:0;width:1200px;height:128px;background:var(--black)}
.site-footer .brand{position:absolute;left:368px;top:52px}
.footer-nav{position:absolute;left:540px;top:58px;display:flex;gap:18px;font-size:9px;color:var(--white);letter-spacing:1px;text-transform:uppercase}
.social{position:absolute;left:796px;top:55px;display:flex;gap:8px}
.social div{width:16px;height:16px;border-radius:50%;background:var(--red)}
</style>
</head>
<body>

<section class="hero abs" role="img" aria-label="Photo of a modern kitchen with island bench and bar stools">
  <h1 class="hero-title abs">Love The Home<br>You're In</h1>
  <a class="btn abs">Get in touch</a>
</section>

<header class="site-header abs">
  <div class="brand"><span class="brand-dot"></span>RW BUILD GROUP</div>
  <nav class="main-nav"><span>Home</span><span>About</span><span>Work</span><span>Contact</span></nav>
  <a class="btn">Call us</a>
</header>

<section class="intro abs">
  <svg class="abs" style="left:0;top:0" width="1200" height="500" viewBox="0 0 1200 500" aria-hidden="true">
    <polygon points="0,0 1200,0 1200,400 0,510" fill="#0c0c0c"/>
  </svg>
  <div class="intro-photo abs photo" role="img" aria-label="Photo of a bathroom with freestanding bath"></div>
  <div class="intro-card abs">
    <p class="eyebrow">Who we are</p>
    <h2>If you can dream it, we can build it.</h2>
    <p class="body-copy">From first sketch to final handover we shape homes around the way you live, with honest advice and care.</p>
    <a class="btn">Find out more</a>
  </div>
</section>

<section class="values abs">
  <div class="values-text abs">
    <p class="eyebrow">Our promise</p>
    <h2>We take pride in our creed that a job isn't finished until our client is absolutely satisfied.</h2>
  </div>
  <div class="value-grid abs">
    <div><h3>Professionalism &amp; Expertise</h3><p class="body-copy">Skilled trades and clear plans on every site.</p></div>
    <div><h3>Trust &amp; Communication</h3><p class="body-copy">Regular updates so you always know where things stand.</p></div>
    <div><h3>Timely</h3><p class="body-copy">Realistic schedules we work hard to keep.</p></div>
    <div><h3>Reasonable</h3><p class="body-copy">Fair, transparent pricing with no surprises.</p></div>
  </div>
  <div class="stair-photo abs photo" role="img" aria-label="Photo of a floating timber staircase"></div>
</section>

<div class="house-photo abs photo" role="img" aria-label="Photo of a modern two storey house at dusk"></div>
<div class="quality-card abs">
  <p class="eyebrow">Our standard</p>
  <h2>At RW Build Group quality counts.</h2>
  <p class="body-copy">We choose proven materials and trusted trades, then check every stage ourselves so the finished home stands up for decades.</p>
  <a class="btn">Our process</a>
</div>

<div class="portfolio-band abs"></div>
<h2 class="portfolio-title abs">Take a look through our portfolio to see the craftsmanship &amp; personal detail into the work we do.</h2>
<div class="tile tile-a abs" role="img" aria-label="Photo of a dark modern living room"><span>Living</span></div>
<div class="tile tile-b abs" role="img" aria-label="Photo of a bedroom interior"><span>Bedroom</span></div>
<div class="tile tile-c abs" role="img" aria-label="Photo of an open plan kitchen"><span>Kitchen</span></div>
<div class="tile tile-d abs" role="img" aria-label="Photo of a dining area"><span>Dining</span></div>

<section class="testimonials abs">
  <div class="testimonials-head abs">
    <p class="eyebrow">Testimonials</p>
    <h2>Don't take our word for it. See what others have to say about us.</h2>
  </div>
  <div class="arrows abs">
    <div><svg width="12" height="10" viewBox="0 0 12 10"><path d="M11 5H1M5 1L1 5l4 4" stroke="#fff" stroke-width="1.5" fill="none"/></svg></div>
    <div><svg width="12" height="10" viewBox="0 0 12 10"><path d="M1 5h10M7 1l4 4-4 4" stroke="#fff" stroke-width="1.5" fill="none"/></svg></div>
  </div>
</section>
<div class="review-row abs">
  <div class="review"><span class="quote">&ldquo;</span><p class="body-copy">The team kept us informed from day one and the finish is better than we imagined.</p><p class="author">Sarah M.</p></div>
  <div class="review"><span class="quote">&ldquo;</span><p class="body-copy">Honest pricing, tidy sites and a home built right on schedule. Highly recommended.</p><p class="author">James T.</p></div>
  <div class="review"><span class="quote">&ldquo;</span><p class="body-copy">They listened to every idea and turned it into a home we love living in.</p><p class="author">Priya K.</p></div>
  <div class="review"><span class="quote">&ldquo;</span><p class="body-copy">Great communication and quality work throughout our renovation.</p><p class="author">Daniel R.</p></div>
</div>

<section class="contact abs">
  <h2>Ready to get started?<br>Let us turn your vision into a reality.</h2>
</section>
<form class="contact-form abs">
  <div class="field">Name</div>
  <div class="field">Email</div>
  <div class="field">Phone</div>
  <div class="field">Subject</div>
  <div class="field wide">Message</div>
</form>
<a class="btn contact-submit abs">Submit</a>

<footer class="site-footer abs">
  <div class="brand"><span class="brand-dot"></span>RW BUILD GROUP</div>
  <nav class="footer-nav"><span>Home</span><span>About</span><span>Work</span><span>Contact</span></nav>
  <div class="social"><div></div><div></div><div></div></div>
</footer>

</body>
</html>
```